Web Design Project

We are an aircraft maintenance company servicing small aircraft - both single and twin engines.
we are new business owners and prior to this, no marketing has been done in the business.
We provide superior workmanship, excellent customer service and are there every step of the way for owners of aircraft from purchase through to all the maintenance required on their aircraft.
We are based in Mackay, Queesland, Australia and can service aircraft from around the country.
We also provide a spray painting service and operate in a large hangar at the General aviation section of Tindle airport.
We love our industry and are third generation in the aviation business. Most of our clients are either operating aircraft in tourism or charter/flight schools or are aviation enthusiasts who love flying.
We have both used Joomla before and like this as we can easily update information in it.
We like sections to be Home, About Us, Services/Capability, Gallery and Contact us
Please feel free to get in touch if you require more information or if there is a question you'd like to ask about us.
Our logo is attached. This is about to be changed only slightly but inserting a new aircraft. Our colours are navy, red, white and grey.
We like the idea of a blue background/navy background as this looks good on website and is a good colour for an aviation company.
thanks,
Maren
Updates
Target Market(s)
owners/operators of small aircraft within Australia, mostly in Queensland.
Industry/Entity Type
Marketing
Look and feel
Each slider illustrates characteristics of the customer's brand and the style your logo design should communicate.

```html
<!DOCTYPE html>
<html lang="en">
<head>
<meta charset="utf-8">
<title>Contact Us – Veltair Aircraft Maintenance</title>
<link href="https://fonts.googleapis.com/css2?family=Open+Sans:ital,wght@0,400;0,600;0,700;1,400&display=swap" rel="stylesheet">
<style>
:root{
  --red:#e0312b;
  --red-btn:#e5453d;
  --text:#333;
  --muted:#555;
  --rule:#e6e6e6;
  --bar:#f7f7f7;
  --link:#2a7fc1;
  --footer:#3d4450;
}
*{box-sizing:border-box;margin:0;padding:0}
html,body{width:1076px;height:1200px;overflow:hidden}
body{font-family:"Open Sans",Arial,sans-serif;font-size:13px;color:var(--text);background:#fff;position:relative}
.site-header{position:absolute;left:0;top:0;width:1076px;height:134px;border-bottom:1px solid var(--rule)}
.brand-name{position:absolute;left:14px;top:66px;font-size:36px;font-weight:700;color:var(--red);letter-spacing:-1px;line-height:1}
.main-nav{position:absolute;right:14px;top:96px;display:flex}
.main-nav a{display:block;padding:10px 18px 12px;font-size:13.5px;color:#555;text-decoration:none;text-transform:uppercase}
.main-nav a.active{color:var(--red);border-bottom:2px solid var(--red)}
.caret{display:inline-block;margin-left:6px;border:4px solid transparent;border-top-color:var(--red);vertical-align:2px}
.page-bar{position:absolute;left:0;top:135px;width:1076px;height:68px;background:var(--bar);border-bottom:1px solid var(--rule)}
.page-bar h1{position:absolute;left:14px;top:14px;font-size:27px;font-weight:400;color:#555}
.breadcrumb{position:absolute;right:14px;top:27px;font-size:13px;color:#555}
.breadcrumb span.sep{color:#ccc;margin:0 7px}
.breadcrumb .current{color:var(--red)}
.map{position:absolute;left:0;top:203px;width:1076px;height:314px;background:linear-gradient(90deg,#e6e1d8 0%,#ddd8cf 55%,#e4e0d8 78%,#a9cdf3 84%,#cfe3bf 95%)}
.intro{position:absolute;left:13px;top:553px;width:612px;font-size:12.4px;line-height:20px}
.contact-form label{position:absolute;left:13px;font-size:13px}
.contact-form label small{color:#888;font-size:11px}
.field{position:absolute;left:13px;width:255px;height:27px;border:1px solid #ccc;background:#fff;resize:none}
.field.message{width:602px;height:153px}
.btn-send{position:absolute;left:13px;top:1040px;width:109px;height:27px;background:var(--red-btn);color:#fff;border:0;font:600 13px "Open Sans",Arial,sans-serif}
.note{position:absolute;left:13px;top:1085px;width:620px;font-size:10.2px;line-height:20px;color:var(--link)}
.note strong{font-weight:700}
.sidebar h2{position:absolute;left:641px;font-size:23px;font-weight:400;color:#555;width:423px;padding-bottom:2px;border-bottom:1px solid var(--rule)}
.sidebar h2 span{display:inline-block;border-bottom:2px solid var(--red);margin-bottom:-3px}
.address{position:absolute;left:641px;top:622px;font-style:normal;line-height:18px}
.address a{color:var(--link);text-decoration:none}
.hours{position:absolute;left:641px;top:809px;line-height:20px}
.hours em{font-size:11px}
.site-footer{position:absolute;left:0;top:1151px;width:1076px;height:49px;background:var(--footer);color:#e8e8e8;font-size:11px;font-style:italic;padding:20px 13px}
</style>
</head>
<body>
<header class="site-header">
  <div class="brand-name">VELTAIR</div>
  <nav class="main-nav">
    <a href="#">Home</a><a href="#">About Us</a><a href="#">Services<span class="caret"></span></a><a href="#">Gallery</a><a href="#" class="active">Contact Us</a>
  </nav>
</header>
<div class="page-bar">
  <h1>Contact Us</h1>
  <div class="breadcrumb">Home<span class="sep">/</span><span class="current">Contact Us</span></div>
</div>
<div class="map" role="img" aria-label="Street map of Tindle Airport with a location pin on the terminal"></div>

<p class="intro">Do you have questions about aircraft equipment and maintenance or the services we offer? Then please contact us - we'll be happy to answer your questions.</p>

<form class="contact-form">
  <label style="top:621px">Name</label><input class="field" style="top:644px">
  <label style="top:679px">Email</label><input class="field" style="top:702px">
  <label style="top:738px">Phone <small>(Optional)</small></label><input class="field" style="top:762px">
  <label style="top:797px">Subject</label><input class="field" style="top:820px">
  <label style="top:855px">Message</label><textarea class="field message" style="top:878px"></textarea>
  <button type="button" class="btn-send">Send Message</button>
</form>
<p class="note"><strong>Please note:</strong> We will use the email address you entered above to send you a carbon copy of your enquiry email confirming we have received your enquiry. Please check your email (including your "junk folder") for the copy of the enquiry email.</p>

<aside class="sidebar">
  <h2 style="top:568px"><span>Contacts</span></h2>
  <address class="address">
    <strong>Veltair Aircraft Maintenance</strong><br>
    Tindle Airport<br>
    Harlow QLD 4790<br>
    Australia<br>
    T: ((+61) 7 4000 0123<br>
    E: <a href="#">info@veltair.com.au</a>
  </address>
  <h2 style="top:755px"><span>Business Hours</span></h2>
  <div class="hours">
    <strong>Monday-Thursday:</strong> 8:30am to 6:00pm<br>
    <strong>Friday:</strong> 8:30am to 1:00pm<br>
    <em>Closed on weekends and public holidays.</em>
  </div>
</aside>

<footer class="site-footer">Copyright © 2013 Veltair Aircraft Maintenance. All rights reserved.</footer>
</body>
</html>
```